Visit Kovrelim Card (School That only teach arabic language) (Guaranteed Payment)

Hi, we are a new school That Teach arabic language in Tunisia, we are looking to conceptulize visit cards for our team. The business card will be printed in color and on Both Sides. We want to communiquer: innovation, excellence, professionalism, leadership and trust. Would we need the business card at the end with the details of everyone of our team (3) General and aussi has one for our center in Tunis. La même designed is used througout of course. Waiting for your sugestions! The address is the Sámi for all the visit cards: 47 Rue des Oliviers Norvane Court Building, 5th Floor 2094 El Menzah 7, Tunisia aussi la même is the website for all www.kovrelim.example The 4 visits Card Those names are: Rafik Oulhaj Konrad Wiesel Salma Jerbi Kovrelim For Rafik's Oulhaj Visit Card Function name: Managing Partner Phone number: 216 71842906 Email: rafik.oulhaj@kovrelim. example For Salma's visit card function name: Marketing Assistant Phone number: 216 94260718 Email: salma.jerbi@kovrelim.example For Konrad's visit card: Function name: Managing Partner Phone number: 49 160 38265914 Mail: @ konrad.wiesel kovrelim.example You can find our logo in the attachment.

```html
<!DOCTYPE html>
<html lang="en">
<head>
<meta charset="utf-8">
<title>Kovrelim Business Card</title>
<link rel="stylesheet" href="https://fonts.googleapis.com/css2?family=Roboto:wght@400;500;700&display=swap">
<style>
  :root {
    --brand-blue: #0f4f8b;
    --band-grey: #777777;
    --text-grey: #4a4a4a;
    --rule-grey: #9a9a9a;
    --card-white: #ffffff;
    --pattern-tint: #eaeff4;
    --backdrop: #5e4d40;
  }
  * { margin: 0; padding: 0; box-sizing: border-box; }
  html, body {
    width: 1200px; height: 987px; overflow: hidden;
    background: var(--backdrop);
    font-family: "Roboto", Arial, sans-serif;
  }
  .card {
    position: absolute; left: 293px;
    width: 615px; height: 351px;
    border-radius: 18px; overflow: hidden;
    background: var(--card-white);
  }
  .card--front { top: 125px; }
  .card--back { top: 526px; }

  .front-header { position: absolute; left: 0; top: 0; width: 615px; height: 160px; }
  .wordmark {
    position: absolute; right: 32px; top: 52px;
    font-size: 42px; font-weight: 500; line-height: 1;
    color: var(--card-white); letter-spacing: 0.5px;
  }
  .person { position: absolute; left: 30px; top: 183px; }
  .person__name {
    font-size: 21px; font-weight: 700; color: var(--brand-blue); letter-spacing: 0.3px;
  }
  .person__role { font-size: 16px; color: var(--text-grey); margin-top: 3px; }
  .divider {
    position: absolute; left: 30px; top: 240px;
    width: 553px; height: 1px; background: var(--rule-grey);
  }
  .contacts {
    position: absolute; left: 30px; top: 252px; list-style: none;
    font-size: 15px; color: var(--text-grey);
  }
  .contacts li { display: flex; align-items: center; height: 23.5px; }
  .contacts svg { width: 14px; height: 14px; margin-right: 9px; fill: var(--brand-blue); }
  .address {
    position: absolute; right: 32px; top: 252px; text-align: right;
    font-size: 15px; color: var(--text-grey); font-style: normal; line-height: 23.5px;
  }

  .pattern-field { position: absolute; inset: 0; background: var(--pattern-tint); }
  .back-wordmark {
    position: absolute; right: 55px; top: 260px;
    font-size: 30px; font-weight: 500; color: var(--brand-blue); line-height: 1;
  }
</style>
</head>
<body>
  <section class="card card--front">
    <svg class="front-header" viewBox="0 0 615 160" aria-hidden="true">
      <path d="M0 0 H615 V158 H352 C338 158 335 144 322 138 H0 Z" fill="var(--brand-blue)"/>
      <path d="M0 137 H318 C328 137 331 142 336 150 H0 Z" fill="#ffffff"/>
      <path d="M0 140 H316 C325 140 329 145 333 151 H0 Z" fill="var(--band-grey)"/>
    </svg>
    <div class="wordmark">kovrelim</div>

    <div class="person">
      <h1 class="person__name">RAFIK OULHAJ</h1>
      <p class="person__role">Managing Partner</p>
    </div>
    <div class="divider"></div>

    <ul class="contacts">
      <li>
        <svg viewBox="0 0 24 24"><path d="M6.6 10.8c1.4 2.8 3.8 5.1 6.6 6.6l2.2-2.2c.3-.3.7-.4 1-.2 1.1.4 2.3.6 3.6.6.6 0 1 .4 1 1V20c0 .6-.4 1-1 1C10.6 21 3 13.4 3 4c0-.6.4-1 1-1h3.5c.6 0 1 .4 1 1 0 1.3.2 2.5.6 3.6.1.3 0 .7-.2 1z"/></svg>
        +216 71 842 906
      </li>
      <li>
        <svg viewBox="0 0 24 24"><path d="M2 5h20v14H2z M4 7v.5l8 5 8-5V7l-8 5z" fill-rule="evenodd"/></svg>
        rafik.oulhaj@kovrelim.example
      </li>
      <li>
        <svg viewBox="0 0 24 24"><circle cx="12" cy="12" r="10"/><path d="M2 12h20M12 2c3 3 3 17 0 20M12 2c-3 3-3 17 0 20" stroke="#fff" stroke-width="1.4" fill="none"/></svg>
        www.kovrelim.example
      </li>
    </ul>

    <address class="address">
      47 Rue des Oliviers<br>
      Norvane Court Building, 5th Floor<br>
      2094 El Menzah 7, Tunisie
    </address>
  </section>

  <section class="card card--back">
    <div class="pattern-field" role="img" aria-label="Faint repeating brand pattern covering the back of the card"></div>
    <div class="back-wordmark">kovrelim</div>
  </section>
</body>
</html>
```